Thank You Card

I'm looking for a thank you card design using our logo and other graphics. We are an essential business and our employees (Electricians) have done an incredible job staying healthy and safe during the COVID-19 pandemic, I want to send each a thank you card.

```html
<!DOCTYPE html>
<html lang="en">
<head>
<meta charset="utf-8">
<title>Thank You Card</title>
<link rel="stylesheet" href="https://fonts.googleapis.com/css2?family=Fira+Sans:wght@900&family=Fira+Sans+Extra+Condensed:wght@700;800&display=swap">
<style>
  :root {
    --card-red: #e8141c;
    --card-red-light: #f2262c;
    --card-red-deep: #c90d16;
    --ink-navy: #15238a;
    --paper-white: #ffffff;
    --page-bg: #f4f4f4;
  }
  html, body {
    margin: 0;
    width: 1200px;
    height: 1200px;
    overflow: hidden;
    background: var(--page-bg);
  }
  .card {
    position: absolute;
    left: 220px;
    top: 60px;
    width: 760px;
    height: 1080px;
    display: block;
    box-shadow: 0 10px 30px rgba(0,0,0,0.18);
  }
  .brand-name {
    font-family: "Fira Sans Extra Condensed", sans-serif;
    font-weight: 800;
    fill: var(--paper-white);
  }
  .headline {
    font-family: "Fira Sans", sans-serif;
    font-weight: 900;
    fill: var(--paper-white);
  }
  .banner-text {
    font-family: "Fira Sans Extra Condensed", sans-serif;
    font-weight: 800;
    fill: var(--ink-navy);
  }
  .footer-line {
    font-family: "Fira Sans Extra Condensed", sans-serif;
    font-weight: 700;
    fill: var(--paper-white);
  }
  .heart { fill: var(--paper-white); }
  .banner-band { fill: none; stroke: var(--paper-white); stroke-linecap: butt; }
</style>
</head>
<body>
<svg class="card" viewBox="0 0 842 1196" xmlns="http://www.w3.org/2000/svg">
  <defs>
    <radialGradient id="burst" cx="50%" cy="55%" r="70%">
      <stop offset="0%" stop-color="var(--card-red-light)"/>
      <stop offset="100%" stop-color="var(--card-red-deep)"/>
    </radialGradient>
    <radialGradient id="corner-tl" cx="0" cy="0" r="1" gradientUnits="userSpaceOnUse" gradientTransform="translate(0 0) scale(300 180)">
      <stop offset="0%" stop-color="#2a2a8e" stop-opacity="0.75"/>
      <stop offset="100%" stop-color="#2a2a8e" stop-opacity="0"/>
    </radialGradient>
    <radialGradient id="corner-tr" cx="0" cy="0" r="1" gradientUnits="userSpaceOnUse" gradientTransform="translate(842 0) scale(320 200)">
      <stop offset="0%" stop-color="#2a2a8e" stop-opacity="0.75"/>
      <stop offset="100%" stop-color="#2a2a8e" stop-opacity="0"/>
    </radialGradient>
    <radialGradient id="corner-bl" cx="0" cy="0" r="1" gradientUnits="userSpaceOnUse" gradientTransform="translate(0 1196) scale(300 200)">
      <stop offset="0%" stop-color="#2a2a8e" stop-opacity="0.75"/>
      <stop offset="100%" stop-color="#2a2a8e" stop-opacity="0"/>
    </radialGradient>
    <radialGradient id="corner-br" cx="0" cy="0" r="1" gradientUnits="userSpaceOnUse" gradientTransform="translate(842 1196) scale(320 220)">
      <stop offset="0%" stop-color="#2a2a8e" stop-opacity="0.75"/>
      <stop offset="100%" stop-color="#2a2a8e" stop-opacity="0"/>
    </radialGradient>
    <path id="arc-top" d="M 175 492 Q 432 319 690 466"/>
    <path id="arc-bottom" d="M 140 905 Q 440 1150 750 897"/>
  </defs>

  <g class="background" role="img" aria-label="Red sunburst background with halftone dot corners">
    <rect width="842" height="1196" fill="url(#burst)"/>
    <rect width="842" height="1196" fill="url(#corner-tl)"/>
    <rect width="842" height="1196" fill="url(#corner-tr)"/>
    <rect width="842" height="1196" fill="url(#corner-bl)"/>
    <rect width="842" height="1196" fill="url(#corner-br)"/>
  </g>

  <g class="brand" text-anchor="middle">
    <text class="brand-name" x="437" y="170" font-size="88" letter-spacing="2">BRIGHTLINE</text>
    <text class="brand-name" x="437" y="270" font-size="96" letter-spacing="2">ELECTRICAL</text>
    <text class="brand-name" x="437" y="310" font-size="36" letter-spacing="1">SERVICES</text>
  </g>

  <g class="banner banner-top">
    <path class="banner-band" d="M 175 478 Q 432 305 690 452" stroke-width="48"/>
    <text class="banner-text" font-size="40" letter-spacing="1">
      <textPath href="#arc-top" startOffset="50%" text-anchor="middle">STAY SAFE • STAY HEALTHY</textPath>
    </text>
  </g>

  <g class="greeting" text-anchor="middle">
    <text class="headline" x="435" y="700" font-size="235" letter-spacing="-6" transform="rotate(-4 435 700)">Thank</text>
    <text class="headline" x="470" y="895" font-size="240" letter-spacing="-6" transform="rotate(-4 470 895)">You!</text>
  </g>

  <g class="banner banner-bottom">
    <path class="banner-band" d="M 140 888 Q 440 1133 750 880" stroke-width="66"/>
    <text class="banner-text" font-size="50" letter-spacing="3">
      <textPath href="#arc-bottom" startOffset="50%" text-anchor="middle">FOR INCREDIBLE JOB</textPath>
    </text>
  </g>

  <g class="hearts">
    <path class="heart" d="M 64 700 C 20 672 14 640 28 624 C 44 606 62 616 66 632 C 74 614 96 610 106 628 C 118 652 96 680 64 700 Z"/>
    <path class="heart" d="M 790 740 C 752 708 740 678 756 660 C 772 644 792 654 796 670 C 804 652 826 648 836 666 C 846 690 826 718 790 740 Z"/>
  </g>

  <text class="footer-line" x="437" y="1108" font-size="40" text-anchor="middle">STAY SAFE • STAY HEALTHY</text>
</svg>
</body>
</html>
```